Social Media Post Quote #5 - Native American Organization

- KINDRED - must be included
- Protect your community. Protect Your Elders. Stay Vaccinated. must be included
- Attached, company Logo, campaign logos and sample flu social media image. - our audience likes BRIGHT colors.
- Must include image from the United States, representing Land/Nature from one of the following regions, Plains and Woodlands, or Southwest, or Mountains, or Coast.
- must include quote: Help our “early elders” achieve “older elders” status.
- One image will be provided twice - incorporating campaign logos - in some fashion
Inspiration: https://velmorastride.org/ and https://www.facebook.com/Velmorastride

```html
<!DOCTYPE html>
<html lang="en">
<head>
<meta charset="utf-8">
<title>Kindred – Protect Your Elders</title>
<link rel="stylesheet" href="https://fonts.googleapis.com/css2?family=Barlow+Condensed:wght@400;500;600;700&family=Montserrat:wght@700&family=Crimson+Pro:wght@500&display=swap">
<style>
  :root {
    --frame: #d9e7e6;
    --teal: #3fa3a6;
    --maroon: #8c4649;
    --cream: #f3ece4;
    --quote-pink: rgba(214, 62, 92, 0.86);
    --white: #ffffff;
    --photo-top: #2e3a1c;
    --photo-mid: #6b4a24;
    --photo-low: #c9526a;
    --photo-water: #3a2a1c;
  }
  html, body {
    margin: 0;
    padding: 0;
    overflow: hidden;
  }
  body {
    width: 1200px;
    height: 1196px;
    background: var(--white);
    font-family: "Barlow Condensed", "Arial Narrow", sans-serif;
  }
  .post {
    position: relative;
    width: 1200px;
    height: 1196px;
    overflow: hidden;
  }
  .frame-pattern {
    position: absolute;
    inset: 0;
    background: var(--frame);
  }
  .nature-photo {
    position: absolute;
    left: 36px;
    top: 36px;
    width: 1128px;
    height: 1124px;
    background:
      radial-gradient(ellipse 40% 30% at 30% 55%, rgba(235, 90, 120, 0.75), transparent 70%),
      radial-gradient(ellipse 38% 30% at 75% 52%, rgba(240, 100, 130, 0.75), transparent 70%),
      linear-gradient(180deg, var(--photo-top) 0%, var(--photo-mid) 45%, var(--photo-low) 70%, var(--photo-water) 100%);
  }
  .campaign-name {
    position: absolute;
    left: 78px;
    top: 93px;
    width: 412px;
  }
  .campaign-name__title {
    display: block;
    height: 80px;
    background: var(--cream);
    border: 4px solid var(--maroon);
    box-sizing: border-box;
    color: var(--teal);
    font-family: "Montserrat", "Arial", sans-serif;
    font-size: 58px;
    font-weight: 700;
    letter-spacing: 3px;
    line-height: 72px;
    text-align: center;
  }
  .campaign-name__subtitle {
    display: block;
    width: 372px;
    margin: 4px 0 0 20px;
    background: var(--maroon);
    color: var(--cream);
    font-family: "Crimson Pro", "Georgia", serif;
    font-size: 17px;
    font-weight: 500;
    line-height: 28px;
    letter-spacing: 0.5px;
    text-align: center;
  }
  .org-name {
    position: absolute;
    right: 60px;
    top: 120px;
    display: flex;
    align-items: center;
    gap: 12px;
    color: var(--teal);
    font-size: 40px;
    font-weight: 600;
  }
  .org-name__dot {
    width: 26px;
    height: 26px;
    border-radius: 50%;
    background: var(--teal);
  }
  .headline {
    position: absolute;
    left: 78px;
    top: 252px;
    margin: 0;
    color: var(--cream);
    font-size: 50px;
    font-weight: 400;
    line-height: 66px;
  }
  .headline__line {
    display: block;
    height: 66px;
    padding-left: 14px;
    background: var(--maroon);
    white-space: nowrap;
  }
  .headline__line strong { font-weight: 700; }
  .headline__line--1 { width: 631px; }
  .headline__line--2 { width: 566px; }
  .headline__line--3 { width: 426px; }
  .step-line {
    position: absolute;
    left: 0;
    top: 0;
  }
  .quote-box {
    position: absolute;
    left: 237px;
    top: 574px;
    width: 728px;
    height: 371px;
    background: var(--quote-pink);
  }
  .quote-box::after {
    content: "";
    position: absolute;
    inset: 6px;
    border: 2px solid var(--white);
  }
  .quote-mark {
    position: absolute;
    left: 0;
    right: 0;
    top: -104px;
    text-align: center;
    color: var(--white);
    font-size: 260px;
    font-weight: 700;
    line-height: 1;
  }
  .quote-text {
    position: absolute;
    left: 0;
    right: 0;
    top: 62px;
    margin: 0;
    text-align: center;
    color: var(--white);
    font-size: 62px;
    font-weight: 400;
    line-height: 66px;
  }
</style>
</head>
<body>
  <main class="post">
    <div class="frame-pattern" role="img" aria-label="Border of teal and maroon zigzag pattern on white"></div>
    <div class="nature-photo" role="img" aria-label="Two roseate spoonbills with bright pink spread wings facing each other in shallow water at sunset"></div>

    <div class="campaign-name">
      <span class="campaign-name__title">KINDRED</span>
      <span class="campaign-name__subtitle">COVID-19 &amp; FLU VACCINATION CAMPAIGN</span>
    </div>

    <div class="org-name">
      <span class="org-name__dot"></span>
      <span>Velmorastride</span>
    </div>

    <svg class="step-line" width="1200" height="1196" aria-hidden="true">
      <polyline points="738,273 738,333 672,333 672,398 525,398 525,462 93,462"
                fill="none" stroke="var(--teal)" stroke-width="5"/>
    </svg>

    <h1 class="headline">
      <span class="headline__line headline__line--1"><strong>PROTECT</strong> YOUR COMMUNITY.</span>
      <span class="headline__line headline__line--2"><strong>PROTECT</strong> YOUR ELDERS.</span>
      <span class="headline__line headline__line--3"><strong>STAY</strong> VACCINATED.</span>
    </h1>

    <section class="quote-box">
      <div class="quote-mark">&ldquo;</div>
      <p class="quote-text">Help our<br>&ldquo;early elders&rdquo;<br>achieve<br>&ldquo;older elders&rdquo; status</p>
    </section>
  </main>
</body>
</html>
```